Long term Care Provider Conference

Banner for LTC providers to know that they can rely on us to deliver high value, cost efficient, professional back office support to streamline operations, improve and maintain compliance with administrative and or nursing solutions for their agency.

Want to update the wording

```html
<!DOCTYPE html>
<html lang="en">
<head>
<meta charset="utf-8">
<title>Norvale Care Solutions – LTC Conference Banner</title>
<link rel="stylesheet" href="https://fonts.googleapis.com/css2?family=Poppins:wght@400;500;600&display=swap">
<style>
  :root {
    --stage: #6b6b6b;
    --paper: #f7f8f9;
    --paper-shade: #e9ecee;
    --ink: #2e3536;
    --teal: #4d6a72;
    --teal-light: #6c8c93;
    --tan: #cdc2bb;
    --tan-deep: #b9aca3;
    --white: #ffffff;
  }
  * { margin: 0; padding: 0; box-sizing: border-box; }
  html, body {
    width: 1200px; height: 840px; overflow: hidden;
    background: var(--stage);
    font-family: "Poppins", sans-serif;
  }
  .banner {
    position: absolute; left: 200px; top: 20px;
    width: 800px; height: 800px; overflow: hidden;
    background: linear-gradient(135deg, var(--white) 0%, var(--paper) 45%, var(--paper-shade) 100%);
  }
  .banner-shapes { position: absolute; inset: 0; }
  .brand {
    position: absolute; top: 52px; left: 0; width: 100%;
    display: flex; justify-content: center; align-items: center; gap: 14px;
  }
  .brand-dot {
    width: 46px; height: 46px; border-radius: 50%;
    background: var(--teal);
  }
  .brand-name {
    font-weight: 600; font-size: 36px; color: var(--teal);
    line-height: 1;
  }
  .headline {
    position: absolute; top: 142px; left: 40px; width: 720px;
    text-align: center; color: var(--ink);
    font-weight: 600; font-size: 35px; line-height: 1.33;
    letter-spacing: -0.3px;
  }
  .benefits {
    position: absolute; top: 312px; left: 58px; width: 300px;
    list-style: none;
  }
  .benefit {
    display: flex; align-items: center; gap: 14px;
    margin-bottom: 34px;
    font-weight: 500; font-size: 15.5px; line-height: 1.3; color: var(--ink);
  }
  .benefit-icon {
    flex: 0 0 44px; width: 44px; height: 48px;
    border: 2px solid var(--teal-light);
    background: var(--tan);
    box-shadow: inset 0 0 0 3px var(--white);
    display: flex; align-items: center; justify-content: center;
  }
  .benefit-icon svg { width: 26px; height: 26px; }
  .photo {
    position: absolute; left: 490px; top: 250px; width: 280px; height: 550px;
    border-radius: 140px 140px 0 0;
    background: linear-gradient(180deg, #d9c4b8 0%, #c9aa98 28%, #4f86b8 55%, #3f74a8 100%);
  }
  .site-url {
    position: absolute; left: 60px; top: 712px;
    color: var(--white); font-weight: 500; font-size: 22px;
    letter-spacing: 8px;
  }
</style>
</head>
<body>
  <main class="banner">
    <svg class="banner-shapes" viewBox="0 0 800 800" width="800" height="800" aria-hidden="true">
      <polygon points="520,0 800,0 800,260 640,430" fill="#eef1f3"/>
      <circle cx="640" cy="540" r="215" fill="var(--teal)"/>
      <path d="M 420 470 A 95 95 0 0 0 420 660 Z" fill="var(--tan)"/>
      <path d="M 0 680 L 560 705 L 640 800 L 0 800 Z" fill="var(--teal)"/>
      <path d="M 330 690 L 560 705 L 640 800 L 420 800 Z" fill="var(--teal-light)" opacity="0.55"/>
    </svg>

    <header class="brand">
      <span class="brand-dot"></span>
      <span class="brand-name">Norvale Care Solutions</span>
    </header>

    <h1 class="headline">LTC Providers Can Rely On Us<br>To Deliver Care Support That<br>Brings High Value</h1>

    <ul class="benefits">
      <li class="benefit">
        <span class="benefit-icon">
          <svg viewBox="0 0 24 24" fill="none" stroke="var(--ink)" stroke-width="1.6"><circle cx="12" cy="12" r="8"/><path d="M14.5 9.5c-.5-1-1.5-1.4-2.5-1.4-1.5 0-2.5.8-2.5 1.9 0 2.6 5 1.4 5 4 0 1.1-1 1.9-2.5 1.9-1.1 0-2.1-.5-2.6-1.4M12 6.5v11"/></svg>
        </span>
        Cost Efficient
      </li>
      <li class="benefit">
        <span class="benefit-icon">
          <svg viewBox="0 0 24 24" fill="none" stroke="var(--ink)" stroke-width="1.6"><rect x="4" y="5" width="16" height="14" rx="1.5"/><path d="M4 10h16M9 14h6"/></svg>
        </span>
        Professional Back Office Support To Streamline Operations
      </li>
      <li class="benefit">
        <span class="benefit-icon">
          <svg viewBox="0 0 24 24" fill="none" stroke="var(--ink)" stroke-width="1.6"><rect x="5" y="4" width="14" height="17" rx="1.5"/><path d="M9 4h6v3H9zM8.5 12l2 2 4-4M8.5 17h7"/></svg>
        </span>
        Improve And Maintain Compliance With Administrative Support
      </li>
      <li class="benefit">
        <span class="benefit-icon">
          <svg viewBox="0 0 24 24" fill="none" stroke="var(--ink)" stroke-width="1.6"><rect x="4" y="4" width="16" height="16" rx="2"/><path d="M12 8v8M8 12h8"/></svg>
        </span>
        Nursing Solutions For Their Agency
      </li>
    </ul>

    <div class="photo" role="img" aria-label="Photo of a smiling nurse in blue scrubs with a stethoscope around her neck, arms crossed"></div>

    <p class="site-url">www.norvale-care.com</p>
  </main>
</body>
</html>
```